Coupons App Design Project

We have a simple coupons app with few screens and actions:
1. Very simple login screen (with chatterloop and findwell+)
2. Very simple business search page
3. Very simple business search results(each result contains logo icon, business name and delete icon)
4. business list (every row contains logo icon, business name and delete icon)
5. coupons list (each item contains image, title, subtitle, description, expiration time, status graphics (valid, expired, redeemed), delete icon
6. coupon view (image, title, subtitle, description, barcode etc.)
7. custom confirmation dialog(title, buttons, background, text)
8. "scan to subscribe" page (merchant name, merchant number, background image, text, barcode to scan etc.)
9. simple menu
10. splash screen

all graphics should be vector graphics so we can use it to different resolutions including for printing
Updates

Hi all, We've increased the project's budget by 25%. Thanks

Hi all,

We've decided to change the project from refundable to committed payment.
FYI

Hi All,

Thank you for your time and efforts, we really appreciate it.However we've eliminated most of the offered designs we've received becausethey didn't fit our desired look and feel.

Please download our look and feel file from our uploaded files -we've put there some examples of other apps that we like.

Thanks

Target Market(s)

shoppers all over the world

Industry/Entity Type

Business

Requirements
Must have
• Please take a look at the attached file "look & feel.jpg" for some nice screen shots taken from apps that we like

Should not have
• *****************************************************************************************
The attached files are only for demonstration purpose and needs descriptions so please don't send us design based on these screenshots.
*****************************************************************************************

```html
<!DOCTYPE html>
<html lang="en">
<head>
<meta charset="utf-8">
<title>Coupons App – Menu</title>
<link rel="stylesheet" href="https://fonts.googleapis.com/css2?family=Lobster&family=Lato:wght@300;400&display=swap">
<style>
  :root {
    --page-bg: #f1f3f4;
    --slate: #6b8ea1;
    --slate-light: #7d9fb0;
    --teal: #3d9491;
    --teal-light: #4aa19e;
    --divider: rgba(255, 255, 255, 0.35);
    --title-text: #ffffff;
    --option-text: #3f5660;
  }

  * { box-sizing: border-box; margin: 0; padding: 0; }

  html, body {
    width: 1200px;
    height: 830px;
    overflow: hidden;
    background: var(--page-bg);
  }

  .canvas {
    width: 1200px;
    height: 830px;
    display: flex;
    align-items: center;
    justify-content: center;
  }

  .menu-screen {
    width: 420px;
    height: 746px;
    background: var(--slate);
    display: flex;
    flex-direction: column;
    box-shadow: 0 10px 30px rgba(0, 0, 0, 0.12);
  }

  .menu-header {
    height: 62px;
    background: linear-gradient(180deg, var(--slate-light), var(--slate));
    display: flex;
    align-items: center;
    justify-content: center;
    border-bottom: 1px solid var(--divider);
  }

  .menu-title,
  .menu-item,
  .sorting-title {
    font-family: "Lobster", cursive;
    color: var(--title-text);
    font-weight: 400;
    text-shadow: 0 1px 1px rgba(0, 0, 0, 0.15);
  }

  .menu-title { font-size: 36px; }

  .menu-list { list-style: none; }

  .menu-item {
    height: 74px;
    background: var(--teal);
    border-bottom: 1px solid var(--divider);
    display: flex;
    align-items: center;
    justify-content: center;
    font-size: 40px;
  }

  .menu-body {
    flex: 1;
    padding: 28px 44px 0;
  }

  .sorting-panel {
    background: var(--teal);
    border: 1px solid var(--divider);
    height: 214px;
    padding-top: 22px;
    text-align: center;
  }

  .sorting-title {
    font-size: 44px;
    line-height: 1;
    margin-bottom: 6px;
  }

  .sorting-options { list-style: none; }

  .sorting-option {
    font-family: "Lato", sans-serif;
    font-weight: 300;
    font-size: 22px;
    line-height: 30px;
    color: var(--option-text);
  }
</style>
</head>
<body>
  <main class="canvas">
    <section class="menu-screen" aria-label="App menu">
      <header class="menu-header">
        <h1 class="menu-title">Menu</h1>
      </header>
      <nav>
        <ul class="menu-list">
          <li class="menu-item">Search Businesses</li>
          <li class="menu-item">Business Listings</li>
          <li class="menu-item">Coupon List</li>
          <li class="menu-item">Scan</li>
        </ul>
      </nav>
      <div class="menu-body">
        <div class="sorting-panel">
          <h2 class="sorting-title">Sorting</h2>
          <ul class="sorting-options">
            <li class="sorting-option">Alphabetical</li>
            <li class="sorting-option">Location</li>
            <li class="sorting-option">Type</li>
          </ul>
        </div>
      </div>
    </section>
  </main>
</body>
</html>
```